Professional, elegant brochure for funeral home

We have a funeral home. We would like a 2 sided brochure. On one side will be 3 columns for our cremation options and on the other side would be 2-3 columns of our burial options. Would like to print it and also will be putting it on our website at www.Veltranoserves.com

Use as examples

https://www.bardwellhaven.com/pricing-and-resources/online-cremation-package-options

https://pellingtonmortuary.com/wp-content/uploads/Cremation-with-Ceremony-Plans.pdf

We only need a simple 1page (front and back brochure). Once we have decided on the designer I can provide the final content to be placed on the brochure.

Target Market(s)

We are family owned business so Something soft, inviting, personable and looks professionally done.

Industry/Entity Type

Funeral Home

Requirements
Must have
• Look professional. Easy to read
Nice to have
• Softer Muted comforting colors. No bright colors.

```html
<!DOCTYPE html>
<html lang="en">
<head>
<meta charset="utf-8">
<title>Veltrano Funeral Home – Cremation Options Flyer</title>
<link href="https://fonts.googleapis.com/css2?family=Montserrat:wght@400;600;700&family=Cormorant+Garamond:wght@500&display=swap" rel="stylesheet">
<style>
  :root{
    --backdrop:#d7e2e2;
    --paper:#ffffff;
    --amber:#e0a15a;
    --navy:#1e3a4f;
    --teal:#6ea3b2;
    --slate:#4f4e48;
    --ink:#1f3346;
    --sans:'Montserrat', Arial, sans-serif;
    --serif:'Cormorant Garamond', Georgia, serif;
  }
  *{box-sizing:border-box;margin:0;padding:0}
  html,body{width:1200px;height:698px;overflow:hidden;background:var(--backdrop)}
  .stage{position:relative;width:1200px;height:698px}
  .flyer{
    position:absolute;left:344px;top:19px;width:552px;height:712px;
    transform:scale(.927);transform-origin:0 0;background:var(--paper);overflow:hidden;
    font-family:var(--sans);
    box-shadow:0 2px 10px rgba(0,0,0,.12);
  }
  .flyer-bg{position:absolute;inset:0}
  .brand{
    position:absolute;left:24px;top:44px;display:flex;align-items:center;gap:8px;
    font-family:var(--sans);font-weight:600;color:var(--ink);font-size:17px;letter-spacing:.5px;
  }
  .brand-dot{width:14px;height:14px;border-radius:50%;background:var(--teal)}
  .option{position:absolute;padding:18px 10px 0 9px;}
  .option p{font-size:10.4px;line-height:13.7px;}
  .option .price{position:absolute;left:8px;font-family:var(--serif);font-weight:500;font-size:40px;line-height:1}
  .price sup{font-size:20px;vertical-align:top;position:relative;top:2px}
  .option--teal{left:30px;top:315px;width:153px;height:300px;background:var(--teal);color:#fff}
  .option--white{left:185px;top:302px;width:182px;height:334px;background:var(--paper);color:var(--ink);padding-top:31px;padding-left:18px}
  .option--white .price{color:var(--amber);left:16px}
  .option--slate{left:367px;top:315px;width:155px;height:300px;background:var(--slate);color:#fff}
  .option--teal .price,.option--slate .price{top:250px}
  .option--white .price{top:263px}
  .contact{position:absolute;display:flex;align-items:center;gap:4px;color:var(--ink);font-size:10.5px;font-weight:600}
  .contact--web{left:12px;top:686px}
  .contact--mail{left:160px;top:686px}
  .contact-sep{position:absolute;left:153px;top:685px;width:1px;height:14px;background:var(--amber)}
  .contact--phone{left:326px;top:672px;font-size:23px;font-weight:700;gap:6px}
</style>
</head>
<body>
<main class="stage">
  <article class="flyer">
    <svg class="flyer-bg" width="552" height="712" viewBox="0 0 552 712" aria-hidden="false">
      <defs>
        <linearGradient id="photoTone" x1="0" y1="0" x2="1" y2="0.4">
          <stop offset="0" stop-color="#e9e3dc"/>
          <stop offset=".45" stop-color="#b58b6c"/>
          <stop offset=".75" stop-color="#5a4b44"/>
          <stop offset="1" stop-color="#24262b"/>
        </linearGradient>
      </defs>
      <polygon points="0,0 552,0 552,245 0,308" fill="url(#photoTone)" role="img" aria-label="Photo of a mourner resting a hand on a wooden casket beside white lilies"/>
      <polygon points="0,308 552,245 552,252 0,316" fill="#ffffff"/>
      <polygon points="0,316 552,252 552,492 0,492" fill="var(--amber)"/>
      <rect x="0" y="492" width="552" height="220" fill="var(--navy)"/>
      <rect x="0" y="672" width="552" height="40" fill="#ffffff"/>
      <polygon points="312,712 322,656 552,656 552,712" fill="#ffffff"/>
    </svg>

    <div class="brand"><span class="brand-dot"></span>Marcus T. Veltrano Funeral Home</div>

    <section class="option option--teal">
      <p>Many people are choosing to cremate, but that doesn’t mean they have to sacrifice the healing elements of a traditional burial. Let us help you create a memorial onsite—because it’s helpful for many families to have a physical marker of remains. We can provide a range of flowers and décor accessories so you can honor your loved one.</p>
      <div class="price"><sup>$</sup>0000</div>
    </section>
    <section class="option option--white">
      <p>Many people are choosing to cremate, but that doesn’t mean they have to sacrifice the healing elements of a traditional burial. Let us help you create a memorial onsite—because it’s helpful for many families to have a physical marker of remains. We can provide a range of flowers and décor accessories so you can honor your loved one.</p>
      <div class="price"><sup>$</sup>0000</div>
    </section>
    <section class="option option--slate">
      <p>Many people are choosing to cremate, but that doesn’t mean they have to sacrifice the healing elements of a traditional burial. Let us help you create a memorial onsite—because it’s helpful for many families to have a physical marker of remains. We can provide a range of flowers and décor accessories so you can honor your loved one.</p>
      <div class="price"><sup>$</sup>0000</div>
    </section>

    <div class="contact contact--web">
      <svg width="12" height="12" viewBox="0 0 12 12"><circle cx="6" cy="6" r="5" fill="none" stroke="#e0a15a" stroke-width="1.2"/><path d="M1 6h10M6 1c2 2 2 8 0 10M6 1c-2 2-2 8 0 10" fill="none" stroke="#e0a15a" stroke-width=".8"/></svg>
      www.veltranofh.com
    </div>
    <span class="contact-sep"></span>
    <div class="contact contact--mail">
      <svg width="12" height="12" viewBox="0 0 12 12"><circle cx="6" cy="6" r="5.4" fill="none" stroke="#e0a15a" stroke-width="1"/><rect x="3" y="4" width="6" height="4.2" fill="none" stroke="#e0a15a" stroke-width=".8"/><path d="M3 4l3 2.3L9 4" fill="none" stroke="#e0a15a" stroke-width=".8"/></svg>
      info@veltranofh.com
    </div>
    <div class="contact contact--phone">
      <svg width="24" height="24" viewBox="0 0 24 24"><circle cx="12" cy="12" r="11" fill="none" stroke="#e0a15a" stroke-width="1.6"/><path d="M8.5 6.5l2 2.2-1.2 1.6c.8 1.7 2 2.9 3.7 3.7l1.6-1.2 2.2 2-1.4 1.9c-4.4-.6-7.8-4-8.4-8.4z" fill="#e0a15a"/></svg>
      (555) 014-2270
    </div>
  </article>
</main>
</body>
</html>
```